Business Card Design Project

New Business Card design for Varodine Technology Ltd using new Logo and new Tagline for staffing company.

About us from our website - www.varodine.example:

VaroDine is a leading and recognized Electronic Entertainment, Workforce Augmentation, and Project Management solutions provider with clients in Electronic Entertainment, Legal, Technology, Government and other verticals that range in size from start up organizations to Zenlar 500 companies. VaroDine is certified as an 8(a) minority and woman owned enterprise, established in 1998.

Target Market(s)

Companies in Electronic Entertainment, Legal, Government and Technology

Industry/Entity Type

Business

Requirements
Must have
• Must include in small letters the following information on back:

Established in 1998
8(a)(w)(e), Cage #7KRT9, DUNS #462137580

Front should have the following:
Derek Holloway
Vice President
5820 Birchmont Road
Fallowby, FB 482917
555-318-2746 X 100
555-902-6613 Fax
555-318-2746 Toll Free
name@varodine.example

Our Tagline: Connect • Collaborate • Achieve

```html
<!DOCTYPE html>
<html lang="en">
<head>
<meta charset="utf-8">
<title>VaroDine Business Card</title>
<link rel="stylesheet" href="https://fonts.googleapis.com/css2?family=Source+Sans+3:ital,wght@0,400;0,600;0,700;1,400&display=swap">
<style>
  :root {
    --page-bg: #e4e4e4;
    --card-white: #ffffff;
    --card-dark: #333333;
    --card-dark-edge: #2a2a2a;
    --ink: #1e1e1e;
    --ink-soft: #6b6b6b;
    --brand-grey: #4a4a4a;
    --brand-blue: #1f6fc0;
    --back-text: #b5b5b5;
  }
  * { box-sizing: border-box; margin: 0; padding: 0; }
  html, body { width: 1200px; height: 900px; overflow: hidden; }
  body {
    background: radial-gradient(ellipse at center, #f2f2f2 0%, var(--page-bg) 75%);
    font-family: "Source Sans 3", "Myriad Pro", sans-serif;
    color: var(--ink);
    position: relative;
  }
  .card {
    position: absolute;
    left: 300px;
    width: 600px;
    height: 343px;
    border-radius: 18px;
    box-shadow: 0 10px 28px rgba(0,0,0,0.22);
  }
  /* Front */
  .card-front { top: 90px; background: var(--card-white); }
  .front-brand {
    position: absolute; left: 36px; top: 112px; width: 250px;
    text-align: center;
  }
  .brand-mark { display: inline-flex; align-items: center; gap: 10px; }
  .brand-dot {
    width: 26px; height: 26px; border-radius: 50%;
    background: var(--brand-blue);
  }
  .brand-name {
    font-weight: 700; font-size: 44px; line-height: 1;
    color: var(--brand-grey); letter-spacing: -0.5px;
  }
  .tagline {
    margin-top: 14px; font-size: 17px; color: var(--brand-blue);
  }
  .website {
    margin-top: 8px; font-size: 18px; color: var(--ink-soft);
  }
  .divider {
    position: absolute; left: 318px; top: 92px;
    width: 2px; height: 120px; background: var(--ink);
  }
  .front-contact { position: absolute; left: 340px; top: 46px; width: 240px; }
  .person-name { font-weight: 600; font-size: 25px; line-height: 1.1; }
  .person-title { font-style: italic; font-size: 20px; color: var(--ink-soft); }
  .company { margin-top: 14px; font-weight: 700; font-size: 19px; line-height: 1.1; }
  .address { font-size: 17px; color: var(--ink-soft); line-height: 1.2; }
  .lines { margin-top: 14px; font-size: 17px; line-height: 1.25; }
  .line { display: flex; }
  .line-label { width: 26px; font-weight: 700; color: var(--ink); }
  .line-value { color: var(--brand-blue); }
  .line-value em { font-style: italic; }
  /* Back */
  .card-back {
    top: 467px;
    background: linear-gradient(160deg, #3c3c3c 0%, var(--card-dark) 55%, var(--card-dark-edge) 100%);
    color: #fff;
  }
  .back-brand {
    position: absolute; left: 0; right: 0; top: 112px;
    display: flex; justify-content: center;
  }
  .back-brand .brand-name { color: #ffffff; font-size: 72px; }
  .back-brand .brand-dot { width: 36px; height: 36px; }
  .back-details {
    position: absolute; left: 0; right: 0; bottom: 34px;
    text-align: center; font-size: 13px; line-height: 1.35;
    color: var(--back-text);
  }
</style>
</head>
<body>
  <section class="card card-front" aria-label="Business card front">
    <div class="front-brand">
      <div class="brand-mark">
        <span class="brand-dot"></span>
        <span class="brand-name">VaroDine</span>
      </div>
      <p class="tagline">Connect • Collaborate • Achieve</p>
      <p class="website">www.varodine.example</p>
    </div>
    <div class="divider"></div>
    <div class="front-contact">
      <p class="person-name">Derek Holloway</p>
      <p class="person-title">Vice President</p>
      <p class="company">VaroDine</p>
      <p class="address">5820 Birchmont Road<br>Fallowby, FB 482917</p>
      <div class="lines">
        <p class="line"><span class="line-label">P</span><span class="line-value">555-318-2746 X 100</span></p>
        <p class="line"><span class="line-label">F</span><span class="line-value">555-902-6613</span></p>
        <p class="line"><span class="line-label"></span><span class="line-value">555-318-2746 <em>(Toll Free)</em></span></p>
        <p class="line"><span class="line-label">E</span><span class="line-value">name@varodine.example</span></p>
      </div>
    </div>
  </section>

  <section class="card card-back" aria-label="Business card back">
    <div class="back-brand">
      <div class="brand-mark">
        <span class="brand-dot"></span>
        <span class="brand-name">VaroDine</span>
      </div>
    </div>
    <div class="back-details">
      <p>Established in 1998</p>
      <p>8(a)(w)(e), Cage #7KRT9, DUNS #462137580</p>
    </div>
  </section>
</body>
</html>
```